Design business cards for Ironvale Barbers (Opening March so won't need finalised till January2018

Ironvale Barbers is the new age barbers and skincare for all men. Creating tailor made haircuts & customised skincare solutions for the perfect healthy manly look. The Barbers will have a industrial, rustic, worldly feel about it. Rustic red brick wall with old wine barrels as the work stations with the old fashion barber chairs. Concrete floor and a bit corrugated iron around.
Target Market(s)
Professional males who like a great haircut, wet shave and may consider a facial if in the right environment. Total pampering experience in a boys environment.
Industry/Entity Type
Barber
Contact Information for Business Card
Front- Logo - address is 42 Kowhai Rd Taupo
Ph - (07) 348 6192
www.ironvalebarbers.com
email - hello@ironvale.co.nz
Back of card
Mens Haircare - Wet Shaving - Facials - Skin Prescriptions
We are doing a loyalty program - 6 squares numbered then 7th free
Colors
Designer to choose colors to be used in the design.
Requirements
Must have
- Clean simple easy to read.
Nice to have
- Our current colours are white font on black background but thinking we need to introduce another colour. Maybe white logo on a copper, bronze or rusty background. Or even a rustic red brick wall with white writing. Want it clean simple to read. Maybe a burgundy?
Should not have
- no images like heads, scissors, razors please

```html
<!DOCTYPE html>
<html lang="en">
<head>
<meta charset="utf-8">
<title>Ironvale Barbers – Business Cards</title>
<link rel="stylesheet" href="https://fonts.googleapis.com/css2?family=Oswald:wght@400;500;600&display=swap">
<style>
  :root {
    --backdrop: #1f1f21;
    --card-black: #1e1c1d;
    --kraft: #b9997b;
    --ink: #2a201b;
    --gold: #bc9d7b;
    --rule: #b5b2ae;
  }
  * { box-sizing: border-box; margin: 0; padding: 0; }
  html, body { width: 1200px; height: 1000px; overflow: hidden; }
  body {
    background: var(--backdrop);
    font-family: "Oswald", "Arial Narrow", sans-serif;
    position: relative;
  }
  .card { position: absolute; left: 205px; width: 790px; height: 450px; overflow: hidden; }
  .card--front { top: 35px; }
  .card--back { top: 510px; background: var(--kraft); }

  .front-info {
    position: absolute; left: 0; top: 0; width: 473px; height: 450px;
    background: var(--card-black); color: var(--gold);
  }
  .brand-name {
    position: absolute; left: 0; width: 100%; text-align: center;
    font-weight: 600; text-transform: uppercase; letter-spacing: 3px; line-height: 1;
  }
  .front-info .brand-name { top: 38px; font-size: 52px; color: var(--gold); }
  .rule { position: absolute; left: 43px; width: 393px; height: 2px; background: var(--rule); }
  .rule--top { top: 201px; }
  .rule--bottom { top: 386px; }
  .contact { position: absolute; left: 58px; top: 212px; font-size: 27px; font-weight: 400; }
  .contact li { list-style: none; display: flex; align-items: center; height: 42px; }
  .contact svg { width: 28px; height: 24px; margin-right: 22px; fill: none; stroke: var(--gold); stroke-width: 2; }
  .contact .address { margin-left: 0; }

  .loyalty {
    position: absolute; left: 473px; top: 0; width: 317px; height: 450px;
    background: var(--kraft); color: var(--ink);
  }
  .loyalty-title {
    position: absolute; top: 30px; width: 100%; text-align: center;
    font-size: 34px; font-weight: 500; letter-spacing: 0.5px;
  }
  .stamp {
    position: absolute; width: 84px; height: 80px; border: 7px solid var(--ink);
    display: flex; align-items: center; justify-content: center;
    font-size: 34px; font-weight: 400;
  }
  .stamp--free { font-size: 28px; }

  .card--back .brand-name { top: 108px; font-size: 86px; color: var(--ink); }
  .services {
    position: absolute; left: 0; bottom: 70px; width: 100%; text-align: center;
    font-size: 24px; font-weight: 500; color: var(--ink); letter-spacing: 0.3px; word-spacing: 2px;
  }
  .services span + span::before { content: "•"; margin: 0 10px; }
</style>
</head>
<body>
  <section class="card card--front">
    <div class="front-info">
      <p class="brand-name">Ironvale<br>Barbers</p>
      <div class="rule rule--top"></div>
      <ul class="contact">
        <li class="address">42 KOWHAI RD, TAUPO</li>
        <li>
          <svg viewBox="0 0 24 24" aria-hidden="true"><path d="M6 3l3 4-2 2c1 3 4 6 7 7l2-2 4 3-2 3C10 20 4 14 3 5z" fill="var(--gold)" stroke="none"/></svg>
          (07) 348 6192
        </li>
        <li>
          <svg viewBox="0 0 24 24" aria-hidden="true"><circle cx="12" cy="12" r="10"/><ellipse cx="12" cy="12" rx="4.5" ry="10"/><path d="M2 12h20M4 7h16M4 17h16M12 2v20"/></svg>
          www.ironvalebarbers.com
        </li>
        <li>
          <svg viewBox="0 0 24 24" aria-hidden="true"><rect x="2" y="5" width="20" height="14" fill="var(--gold)" stroke="none"/><path d="M2 5l10 8 10-8" stroke="var(--card-black)"/></svg>
          hello@ironvale.co.nz
        </li>
      </ul>
      <div class="rule rule--bottom"></div>
    </div>
    <div class="loyalty">
      <h2 class="loyalty-title">LOYALTY PROGRAM</h2>
      <div class="stamp" style="left:19px;top:112px">1</div>
      <div class="stamp" style="left:19px;top:206px">2</div>
      <div class="stamp" style="left:19px;top:301px">3</div>
      <div class="stamp" style="left:112px;top:112px">4</div>
      <div class="stamp" style="left:112px;top:206px">5</div>
      <div class="stamp" style="left:112px;top:301px">6</div>
      <div class="stamp stamp--free" style="left:204px;top:206px">FREE</div>
    </div>
  </section>

  <section class="card card--back">
    <p class="brand-name">Ironvale<br>Barbers</p>
    <p class="services"><span>MENS HAIRCARE</span><span>WET SHAVING</span><span>FACIALS</span><span>SKIN PRESCRIPTIONS</span></p>
  </section>
</body>
</html>
```